Website redesign

Looking to redesign our existing website. (quill7meadows.com.au)
New design needs to be bright, fun and have an easy flowing.
The website needs to be design with call to action.

Some examples of other websites:
fernquaylo.com
tovanmilk.com.au

We are happy with the content of our existing website.

Target Market(s)

other businesses

Industry/Entity Type

Business Service

Number of Pages Required

5+ page

Requirements
Must have
• Theme redesign
Cool animation similar to fernquaylo.com

```html
<!DOCTYPE html>
<html lang="en">
<head>
<meta charset="utf-8">
<title>Quill7 Meadows — Virtual Assistants</title>
<link rel="stylesheet" href="https://fonts.googleapis.com/css2?family=Poppins:wght@400;500;600;700;800&family=Arimo:wght@400;700&display=swap">
<style>
:root{
  --blue:#1fa6de;
  --blue-deep:#1687c2;
  --navy:#0c2f3d;
  --ink:#2b2b2b;
  --muted:#555;
  --line:#c9c9c9;
  --paper:#ffffff;
  --mist:#f3f4f5;
}
*{box-sizing:border-box;margin:0;padding:0}
html,body{width:1200px;height:4230px;overflow:hidden}
body{position:relative;background:var(--paper);font-family:"Arimo",Arial,sans-serif;color:var(--ink)}
.abs{position:absolute}
.heading{font-family:"Poppins",Arial,sans-serif}

/* top bar */
.topbar{left:0;top:0;width:1200px;height:30px;background:var(--navy);color:#fff;font-size:13px}
.topbar .item{position:absolute;top:8px;display:flex;align-items:center;gap:10px}
.topbar svg{width:14px;height:14px}
.socials{position:absolute;display:flex;gap:10px}
.socials span{width:12px;height:12px;border-radius:50%;background:currentColor;display:block}

/* nav */
.nav{left:0;top:30px;width:1200px;height:73px;background:#fff}
.brand{position:absolute;font-family:"Poppins",sans-serif;font-weight:700;color:var(--navy);display:flex;align-items:center;gap:8px}
.brand i{display:block;border-radius:50%;background:var(--blue)}
.nav .brand{left:90px;top:16px;font-size:32px}
.nav .brand i{width:14px;height:14px}
.menu a{position:absolute;top:34px;font-family:"Poppins",sans-serif;font-size:13.5px;font-weight:500;color:#444;text-decoration:none;letter-spacing:.3px}
.menu a.active{color:var(--navy)}
.menu a.active::after{content:"";position:absolute;left:0;right:0;bottom:-6px;height:2px;background:var(--blue)}
.btn{position:absolute;background:var(--blue);color:#fff;font-family:"Poppins",sans-serif;font-weight:700;letter-spacing:1px;border-radius:20px;display:flex;align-items:center;justify-content:center;text-decoration:none;box-shadow:0 3px 6px rgba(0,0,0,.2)}

/* hero */
.hero-photo{left:0;top:103px;width:1200px;height:529px;background:linear-gradient(100deg,#d9dcdf 0%,#eef0f1 45%,#cfd3d6 70%,#9ea5a8 100%)}
.hero-title{left:140px;top:272px;font-family:"Poppins",sans-serif;font-weight:700;font-size:35px;color:#fff;text-shadow:0 1px 3px rgba(0,0,0,.25)}
.hero-sub{left:136px;top:312px;font-size:28px;color:#1b1b1b;font-family:"Arimo",sans-serif}
.hero-rule{top:382px;height:1px;background:#fff;width:120px}

/* intro band */
.intro{left:0;top:632px;width:602px;height:396px;background:var(--blue)}
.intro h2{position:absolute;left:89px;top:70px;width:370px;font-family:"Poppins",sans-serif;font-weight:700;font-size:25px;line-height:32px;color:#fff}
.intro p{position:absolute;left:89px;top:190px;width:370px;font-size:14.5px;line-height:19px;color:#fff}
.video{left:602px;top:632px;width:598px;height:396px;background:linear-gradient(90deg,#2f8fd0 0%,#63a9d8 35%,#1d6fb0 60%,#1a5e9a 100%)}
.person{position:absolute;color:#fff;font-family:"Poppins",sans-serif}
.person b{display:block;font-size:31px;font-weight:500;line-height:36px}
.person small{display:block;font-family:"Arimo",sans-serif;font-size:17px}

/* process */
.doodles{left:0;top:1075px;width:1200px;height:1160px;background:var(--mist);opacity:.75}
.section-title{position:absolute;left:0;width:1200px;text-align:center;font-family:"Poppins",sans-serif;font-weight:700;font-size:31px;color:#111}
.step{position:absolute;left:179px;width:845px;height:151px;border:1px solid var(--line);background:#fff}
.step .tab{position:absolute;top:-1px;width:140px;height:152px;background:var(--blue);color:#fff;text-align:center;font-family:"Poppins",sans-serif}
.step .tab::after{content:"";position:absolute;top:50%;margin-top:-32px;border:32px solid transparent}
.step.left .tab{left:-1px}
.step.left .tab::after{left:140px;border-left:32px solid var(--blue);border-right:0}
.step.right .tab{right:-1px}
.step.right .tab::after{right:140px;border-right:32px solid var(--blue);border-left:0}
.tab .lbl{display:block;margin-top:28px;font-size:26px;font-weight:500;line-height:30px}
.tab .num{display:block;font-size:58px;font-weight:600;line-height:64px}
.step h3{position:absolute;font-family:"Poppins",sans-serif;font-weight:600;font-size:20px;color:var(--blue)}
.step p{position:absolute;font-size:14px;line-height:19px;color:#333}
.step.left h3,.step.left p{left:220px;width:570px}
.step.right h3,.step.right p{left:37px;width:570px}

/* services */
.service{position:absolute;width:200px;text-align:center}
.service svg{display:block;margin:0 auto}
.service h4{margin-top:28px;font-family:"Arimo",sans-serif;font-weight:700;font-size:20px;line-height:26px;color:#555}
.tagline{left:0;top:2676px;width:1200px;text-align:center;font-family:"Poppins",sans-serif;font-weight:600;font-size:20px;line-height:26px;color:#555}

/* why band */
.why{left:0;top:2791px;width:602px;height:352px;background:var(--blue)}
.why-photo{left:602px;top:2791px;width:598px;height:352px;background:linear-gradient(110deg,#c9d3dc 0%,#7f8a94 40%,#2c3e55 70%,#d7dde3 100%)}
.why h2{position:absolute;left:179px;top:58px;font-family:"Poppins",sans-serif;font-weight:700;font-size:21px;color:#fff}
.why .sub{position:absolute;left:179px;top:86px;font-family:"Poppins",sans-serif;font-style:italic;font-weight:600;font-size:14px;color:#fff}
.why ul{position:absolute;left:182px;top:133px;list-style:none}
.why li{position:relative;padding-left:28px;font-weight:700;font-size:15.5px;line-height:26.5px;color:#fff}
.why li::before{content:"";position:absolute;left:0;top:11px;width:6px;height:6px;border-radius:50%;background:#fff}

/* quote */
.field{position:absolute;border:1.5px solid #8a8a8a;border-radius:4px;background:#fff;font-size:14px;color:#777;padding:22px 20px}
.field.msg{padding-top:16px}
.sketch{position:absolute;background:#e9ecee;border-radius:8px}

/* footer */
.footer-line{left:0;top:3727px;width:1200px;height:1px;background:#e3e3e3}
.footer-brand{left:0;top:3752px;width:1200px;text-align:center}
.footer-brand .brand{position:static;justify-content:center;font-size:34px}
.footer-brand .brand i{width:14px;height:14px}
.footer-brand .name{font-family:"Poppins",sans-serif;font-size:19px;color:var(--navy);margin-top:2px}
.col{position:absolute;top:3890px}
.col h5{font-family:"Poppins",sans-serif;font-weight:700;font-size:17px;color:var(--blue-deep);margin-bottom:14px}
.col a,.col span{display:block;font-size:15px;line-height:38px;color:#666;text-decoration:none}
.col.contact span{line-height:46px}
.to-top{left:1028px;top:4031px;width:54px;height:54px;border-radius:50%;background:var(--blue-deep)}
.bottom{left:0;top:4163px;width:1200px;height:67px;background:var(--blue-deep);color:#fff;font-size:14px}
.bottom p{position:absolute;left:177px;top:28px}
</style>
</head>
<body>

<header class="abs topbar">
  <div class="item" style="left:88px">
    <svg viewBox="0 0 16 16"><path d="M3 1l3 3-2 2c1 2 3 4 5 5l2-2 3 3-2 3C7 15 1 9 1 3z" fill="#29abe2"/></svg>
    <span>07 3900 4417</span>
  </div>
  <div class="item" style="left:262px">
    <svg viewBox="0 0 16 12"><rect x="1" y="1" width="14" height="10" fill="none" stroke="#29abe2" stroke-width="1.5"/><path d="M1 1l7 6 7-6" fill="none" stroke="#29abe2" stroke-width="1.5"/></svg>
    <span>arun@quill7meadows.com.au</span>
  </div>
  <div class="item" style="left:534px">
    <svg viewBox="0 0 16 12"><rect x="1" y="1" width="14" height="10" fill="none" stroke="#29abe2" stroke-width="1.5"/><path d="M1 1l7 6 7-6" fill="none" stroke="#29abe2" stroke-width="1.5"/></svg>
    <span>tomas@quill7meadows.com.au</span>
  </div>
  <div class="socials" style="left:916px;top:9px;color:#fff"><span></span><span></span><span></span><span></span></div>
</header>

<nav class="abs nav">
  <div class="brand">Q7M<i></i></div>
  <div class="menu">
    <a class="active" href="#" style="left:424px">HOME</a>
    <a href="#" style="left:509px">OUR STORY</a>
    <a href="#" style="left:645px">SERVICES</a>
    <a href="#" style="left:770px">TIPS &amp; TRICKS</a>
    <a href="#" style="left:924px">FAQ</a>
  </div>
  <a class="btn" href="#" style="left:993px;top:21px;width:113px;height:36px;font-size:14px">CONTACT</a>
</nav>

<section>
  <div class="abs hero-photo" role="img" aria-label="Smiling woman working on a laptop at a bright office desk with plants"></div>
  <h1 class="abs hero-title">VIRTUAL ASSISTANT?</h1>
  <p class="abs hero-sub">MORE LIKE VALUABLE ASSET!</p>
  <div class="abs hero-rule" style="left:148px"></div>
  <div class="abs hero-rule" style="left:396px"></div>
  <a class="btn" href="#" style="left:271px;top:366px;width:113px;height:32px;font-size:15px">DISCOVER</a>
</section>

<section>
  <div class="abs intro">
    <h2>Outsourcing. A big word that means big things for your business.</h2>
    <p>Virtual Assistants are the superheroes of the modern office. They can do everything your team can do on a computer at a fraction of the price! (Well, maybe not high five you when you've had a win, but a virtual high five is definitely on the table!)</p>
    <a class="btn" href="#" style="left:87px;top:322px;width:113px;height:32px;font-size:15px">EXPLORE</a>
  </div>
  <div class="abs video" role="img" aria-label="Video still of the two company founders speaking to camera"></div>
  <svg class="abs" style="left:865px;top:772px" width="82" height="82" viewBox="0 0 82 82"><circle cx="41" cy="41" r="41" fill="#fff"/><path d="M33 25l24 16-24 16z" fill="#1fa6de"/></svg>
  <div class="person" style="left:602px;top:937px"><b>Tomas Berwick</b><small>tomas@quill7meadows.com.au</small></div>
  <div class="person" style="right:7px;top:937px;text-align:right"><b>Arun Delford</b><small>arun@quill7meadows.com.au</small></div>
</section>

<section>
  <div class="abs doodles" role="img" aria-label="Faint hand-drawn business doodles: gears, charts, dollar signs, robot"></div>
  <h2 class="section-title" style="top:1084px">THE PROCESS</h2>

  <article class="step left" style="top:1167px">
    <div class="tab"><span class="lbl">STEP</span><span class="num">01</span></div>
    <h3 style="top:20px">Provide Your Preferred Qualifications.</h3>
    <p style="top:55px">Set up a call with our team to specify the requirements and qualifications you're searching for in a Virtual Assistant. This will be our checklist for your perfect assistant! From there, we'll take care of shortlisting, testing, background checking and recruiting.</p>
  </article>

  <article class="step right" style="top:1367px">
    <div class="tab"><span class="lbl">STEP</span><span class="num">02</span></div>
    <h3 style="top:24px">Endorsing the Shortlisted Candidates</h3>
    <p style="top:59px">After the thorough vetting process, we'll put forward the best candidate. You can then conduct the final interview on your preferred communication platform at a time that suits you. Once the schedule is set, we'll let the candidates know!</p>
  </article>

  <article class="step left" style="top:1571px">
    <div class="tab"><span class="lbl">STEP</span><span class="num">03</span></div>
    <h3 style="top:34px">Conducting the Final Interview</h3>
    <p style="top:69px">The final interview is the perfect time to get to know the candidates. It'll help to have a list of questions prepared that will help you pick out the chosen one!</p>
  </article>

  <article class="step right" style="top:1773px">
    <div class="tab"><span class="lbl">STEP</span><span class="num">04</span></div>
    <h3 style="top:26px">Setting up the Tools</h3>
    <p style="top:61px">Once you've chosen your Virtual Assistant, it's time for their system to be set up. You can get your own IT team onto the installation, otherwise, we've got a super team of tech peeps who can do it for you.</p>
  </article>

  <article class="step left" style="top:1975px">
    <div class="tab"><span class="lbl">STEP</span><span class="num">03</span></div>
    <h3 style="top:20px">Your Magical Journey Begins</h3>
    <p style="top:55px">Now you and your Virtual Assistant are all set up and ready to rumble! Feel the magic of having a reliable assistant to take on all the menial, repetitive, time-consuming tasks, and focus your energy on more important things. Meet new clients, explore business opportunities, or just spend some time with friends and family!</p>
  </article>
</section>

<section>
  <h2 class="section-title" style="top:2267px">OUR SERVICES</h2>
  <div class="service" style="left:138px;top:2379px">
    <svg width="150" height="150" viewBox="0 0 150 150"><path d="M106 19A64 64 0 1 0 131 45" fill="none" stroke="#1fa6de" stroke-width="17"/><rect x="50" y="50" width="50" height="50" rx="6" fill="#e3e6e8" role="img" aria-label="Recruitment icon"/></svg>
    <h4>We recruit<br>Virtual Assistants</h4>
  </div>
  <div class="service" style="left:381px;top:2379px">
    <svg width="150" height="150" viewBox="0 0 150 150"><path d="M106 19A64 64 0 1 0 131 45" fill="none" stroke="#1fa6de" stroke-width="17"/><rect x="50" y="50" width="50" height="50" rx="6" fill="#e3e6e8" role="img" aria-label="Tech support icon"/></svg>
    <h4>Provide the tech<br>support for these<br>superheroes</h4>
  </div>
  <div class="service" style="left:622px;top:2379px">
    <svg width="150" height="150" viewBox="0 0 150 150"><path d="M106 19A64 64 0 1 0 131 45" fill="none" stroke="#1fa6de" stroke-width="17"/><rect x="50" y="50" width="50" height="50" rx="6" fill="#e3e6e8" role="img" aria-label="Phone system icon"/></svg>
    <h4>Set up the phone<br>system (their own<br>Hero Phone!)</h4>
  </div>
  <div class="service" style="left:864px;top:2379px">
    <svg width="150" height="150" viewBox="0 0 150 150"><path d="M106 19A64 64 0 1 0 131 45" fill="none" stroke="#1fa6de" stroke-width="17"/><rect x="50" y="50" width="50" height="50" rx="6" fill="#e3e6e8" role="img" aria-label="Management document icon"/></svg>
    <h4>We manage &amp;<br>and keep them in<br>tip-top shape!</h4>
  </div>
  <p class="abs tagline">See? It's that simple! The only thing to do now is to finally get started<br>on the quote... just scroll down a little more.</p>
</section>

<section>
  <div class="abs why">
    <h2>IT'S TIME FOR QUILL7 MEADOWS</h2>
    <p class="sub">Why are we your new best outsourcing friend?</p>
    <ul>
      <li>Your Own Virtual Assistant</li>
      <li>One Invoice Per Month</li>
      <li>No Super or TAX</li>
      <li>Dedicated To Your Business Only</li>
      <li>Dedicated Phone System</li>
      <li>IT Setup and Support</li>
    </ul>
  </div>
  <div class="abs why-photo" role="img" aria-label="Business team in an office with two colleagues shaking hands"></div>
</section>

<section>
  <h2 class="section-title" style="top:3195px;font-size:30px;font-weight:600">Get a Quote</h2>
  <div class="sketch" style="left:66px;top:3333px;width:112px;height:140px" role="img" aria-label="Sketch of a mobile phone ringing"></div>
  <div class="sketch" style="left:1010px;top:3490px;width:92px;height:82px" role="img" aria-label="Sketch of an email envelope"></div>
  <div class="field" style="left:218px;top:3277px;width:368px;height:55px;padding-top:17px">Name</div>
  <div class="field" style="left:606px;top:3277px;width:368px;height:55px;padding-top:17px">Phone</div>
  <div class="field" style="left:218px;top:3367px;width:368px;height:56px;padding-top:17px">Email</div>
  <div class="field" style="left:606px;top:3367px;width:368px;height:56px;padding-top:17px">Subject</div>
  <div class="field msg" style="left:218px;top:3457px;width:756px;height:140px">Message</div>
  <a class="btn" href="#" style="left:543px;top:3633px;width:112px;height:33px;font-size:15px">SUBMIT</a>
</section>

<footer>
  <div class="abs footer-line"></div>
  <div class="abs footer-brand">
    <div class="brand">Q7M<i></i></div>
    <p class="name">QUILL7 MEADOWS</p>
  </div>
  <div class="col" style="left:176px">
    <h5>Menu</h5>
    <a href="#">Home</a><a href="#">Services</a><a href="#">Our Story</a><a href="#">FAQ's</a><a href="#">Tips &amp; Tricks</a>
  </div>
  <div class="col" style="left:369px">
    <h5>Useful Link</h5>
    <a href="#">Terms &amp; Condition</a><a href="#">Privacy Policy</a><a href="#">Copy Rights</a>
  </div>
  <div class="col contact" style="left:584px">
    <h5>Contact</h5>
    <span>Phone: 07 3900 4417</span><span>arun@quill7meadows.com.au</span><span>tomas@quill7meadows.com.au</span>
  </div>
  <div class="col" style="left:926px">
    <h5>Follow Us</h5>
    <div class="socials" style="position:static;color:#888"><span></span><span></span><span></span><span></span></div>
  </div>
  <svg class="abs to-top" viewBox="0 0 54 54"><path d="M17 31l10-10 10 10" fill="none" stroke="#fff" stroke-width="4" stroke-linecap="round" stroke-linejoin="round"/></svg>
  <div class="abs bottom"><p>© 2020 quill7meadows.com.au. All rights reserved.</p></div>
</footer>

</body>
</html>
```